Geschäftspapiere für Unternehmensberatung
Zielgruppe
Wir machen Unternehmensberatung, Prozessoptimierung, Change Management,
Buchhaltung.
Unsere Zielgruppe sind Firmen, denen es wirtschaftlich nicht so gut geht und die Hilfe benötigen.
Aufgabenstellung
Wir möchten ein CI an unser Logo angepasst.
Es darf gerne etwas besonderes sein.

```html
<!DOCTYPE html>
<html lang="de">
<head>
<meta charset="utf-8">
<title>Brelton Consulting – Briefumschläge</title>
<link href="https://fonts.googleapis.com/css2?family=Open+Sans:wght@400;600&display=swap" rel="stylesheet">
<style>
  :root {
    --bg: #f1f1f1;
    --paper: #ffffff;
    --brand-blue: #175193;
    --window: #f2f2f2;
    --window-edge: #dcdcdc;
    --mark-faint: #f3f3f3;
    --text-grey: #555a60;
    --shadow: rgba(0,0,0,0.12);
  }
  html, body {
    margin: 0;
    padding: 0;
    width: 1200px;
    height: 948px;
    overflow: hidden;
    background: var(--bg);
    font-family: "Open Sans", sans-serif;
  }
  .canvas {
    position: relative;
    width: 1200px;
    height: 948px;
  }
  .envelope {
    position: absolute;
    width: 560px;
    height: 280px;
    background: var(--paper);
    box-shadow: 0 6px 18px var(--shadow);
    overflow: hidden;
  }
  /* Rückseite */
  .envelope--back { left: 560px; top: 90px; }
  .envelope--back .flap {
    position: absolute;
    inset: 0;
    width: 100%;
    height: 100%;
  }
  .envelope--back .brand-name {
    position: absolute;
    left: 0;
    right: 0;
    top: 58px;
    text-align: center;
    color: var(--paper);
    font-weight: 600;
    font-size: 17px;
    letter-spacing: 0.5px;
  }
  .envelope--back .sender-line {
    position: absolute;
    left: 0;
    right: 0;
    bottom: 56px;
    text-align: center;
    font-size: 8px;
    color: var(--text-grey);
  }
  /* Vorderseite */
  .envelope--front { left: 80px; top: 540px; }
  .band-top {
    position: absolute;
    left: 0;
    top: 0;
    width: 320px;
    height: 14px;
    background: var(--brand-blue);
    border-bottom-right-radius: 6px;
  }
  .band-bottom {
    position: absolute;
    right: 0;
    bottom: 0;
    width: 330px;
    height: 14px;
    background: var(--brand-blue);
    border-top-left-radius: 6px;
  }
  .envelope--front .brand {
    position: absolute;
    left: 34px;
    top: 36px;
    display: flex;
    align-items: center;
    gap: 10px;
  }
  .brand .dot {
    width: 22px;
    height: 22px;
    border-radius: 50%;
    background: var(--brand-blue);
  }
  .envelope--front .brand-name {
    color: var(--brand-blue);
    font-weight: 600;
    font-size: 20px;
    letter-spacing: 0.5px;
  }
  .address-window {
    position: absolute;
    left: 34px;
    top: 100px;
    width: 230px;
    height: 120px;
    background: var(--window);
    border: 1px solid var(--window-edge);
    border-radius: 12px;
  }
  .faint-circle {
    position: absolute;
    right: 40px;
    top: 110px;
    width: 150px;
    height: 150px;
    border-radius: 50%;
    border: 6px solid var(--mark-faint);
  }
</style>
</head>
<body>
<main class="canvas">

  <section class="envelope envelope--back" aria-label="Umschlag Rückseite">
    <svg class="flap" viewBox="0 0 560 280" aria-hidden="true">
      <path d="M0 0 H560 V150 L520 178 Q514 182 506 182 H14 Q0 182 0 168 Z" fill="var(--brand-blue)"/>
    </svg>
    <div class="brand-name">Brelton Consulting</div>
    <div class="sender-line">brelton-consulting UG | Lindenweg 12 | 26100 Nordhafen</div>
  </section>

  <section class="envelope envelope--front" aria-label="Umschlag Vorderseite">
    <div class="band-top"></div>
    <div class="brand">
      <span class="dot"></span>
      <span class="brand-name">Brelton Consulting</span>
    </div>
    <div class="address-window"></div>
    <div class="faint-circle"></div>
    <div class="band-bottom"></div>
  </section>

</main>
</body>
</html>
```